Bref créative
PeakMotion Chiropractic stationary
Simple
PeakMotion Chiropractic Inc.
Colin R Dembry D.C.
5917 S 420 E Bld. 200 Ste C.
Hollin Ridge, IN 46273
(inside Norrin Callow Fitness Center)
dembrydc@qvmail.example
will ad later
Try to implement this tag line
"work hard, play hard, safe guard"
place for next appointment
can upload different formats, just let me know

```html
<!DOCTYPE html>
<html lang="en">
<head>
<meta charset="utf-8">
<title>PeakMotion Chiropractic Stationery</title>
<link href="https://fonts.googleapis.com/css2?family=Montserrat:wght@400;600;700&family=Open+Sans:wght@400;600;700&display=swap" rel="stylesheet">
<style>
:root{
  --bg:#e9e9ec;
  --paper:#ffffff;
  --ink:#4a4f5a;
  --brand:#5d6878;
  --accent-blue:#2a4fb8;
  --accent-purple:#6a2aa8;
  --accent-red:#d8262a;
  --accent-orange:#f5871f;
  --accent-yellow:#fcd116;
  --faint:#f3e4ec;
}
*{box-sizing:border-box;margin:0;padding:0}
html,body{width:1200px;height:912px;overflow:hidden;background:var(--bg)}
body{position:relative;font-family:"Open Sans",sans-serif;color:var(--ink)}
.sheet{position:absolute;background:var(--paper);box-shadow:0 2px 10px rgba(0,0,0,.18);overflow:hidden}

.brand{display:flex;align-items:center;gap:10px;position:relative;z-index:1}
.brand-dot{border-radius:50%;background:var(--accent-blue);flex:none}
.brand-name{font-family:"Montserrat",sans-serif;font-weight:600;color:var(--brand);letter-spacing:.5px;white-space:nowrap}

.deco-circle{position:absolute;border-radius:50%;background:var(--faint);z-index:0}

.tagline-band{position:absolute;display:flex;align-items:center;justify-content:center;z-index:2}
.tagline{color:#fff;font-family:"Montserrat",sans-serif;font-weight:700;white-space:nowrap;transform:rotate(-90deg)}

/* Letterhead */
.letterhead{left:575px;top:40px;width:600px;height:776px}
.letterhead .stripe{position:absolute;left:0;top:0;width:22px;height:100%;
  background:linear-gradient(180deg,var(--accent-yellow),var(--accent-orange) 45%,var(--accent-red))}
.letterhead .brand{position:absolute;left:60px;top:48px}
.letterhead .brand-dot{width:34px;height:34px}
.letterhead .brand-name{font-size:26px}
.letterhead .body{position:absolute;left:60px;top:150px;width:470px;font-size:8.5px;line-height:1.55;z-index:1}
.letterhead .body h2{font-size:10px;font-weight:700;margin-bottom:10px;color:#222}
.letterhead .body p{margin-bottom:10px}
.letterhead .deco-circle{width:330px;height:330px;right:-60px;top:330px}

/* Envelope */
.envelope{left:30px;top:160px;width:520px;height:270px}
.envelope .tagline-band{left:0;top:0;width:44px;height:100%;
  background:linear-gradient(180deg,var(--accent-yellow),var(--accent-orange) 30%,var(--accent-red) 55%,var(--accent-purple) 80%,var(--accent-blue))}
.envelope .tagline{font-size:11px}
.envelope .brand{position:absolute;left:64px;top:30px}
.envelope .brand-dot{width:26px;height:26px}
.envelope .brand-name{font-size:19px}
.envelope .deco-circle{width:200px;height:200px;right:30px;top:80px}

/* Appointment card */
.appointment-card{left:200px;top:460px;width:340px;height:195px}
.appointment-card .tagline-band{right:0;top:0;width:30px;height:100%;
  background:linear-gradient(180deg,var(--accent-red),var(--accent-purple) 60%,var(--accent-blue))}
.appointment-card .tagline{font-size:8px}
.appointment-card .brand{position:absolute;left:22px;top:20px}
.appointment-card .brand-dot{width:18px;height:18px}
.appointment-card .brand-name{font-size:14px}
.appointment-card .fields{position:absolute;left:24px;top:72px;width:200px;font-size:10px;font-weight:600;z-index:1}
.appointment-card .field{display:flex;align-items:flex-end;gap:6px;height:26px}
.appointment-card .field span{flex:1;border-bottom:1px solid #999;height:1px;margin-bottom:3px}
.appointment-card .deco-circle{width:130px;height:130px;right:50px;top:50px}

/* Business card */
.business-card{left:30px;top:690px;width:340px;height:195px}
.business-card .tagline-band{left:0;top:0;width:30px;height:100%;
  background:linear-gradient(180deg,var(--accent-yellow),var(--accent-orange) 30%,var(--accent-red) 60%,var(--accent-blue))}
.business-card .tagline{font-size:8px}
.business-card .brand{position:absolute;left:48px;top:22px}
.business-card .brand-dot{width:18px;height:18px}
.business-card .brand-name{font-size:14px}
.business-card .person{position:absolute;left:48px;top:70px;font-size:10px;font-weight:700;color:#333;z-index:1}
.business-card .contact{position:absolute;left:48px;top:92px;font-size:7.5px;line-height:1.5;z-index:1}
.business-card .contact .label{font-weight:700}
.business-card .deco-circle{width:140px;height:140px;right:-20px;top:60px}
</style>
</head>
<body>

<section class="sheet letterhead" aria-label="Letterhead">
  <div class="stripe"></div>
  <div class="brand"><span class="brand-dot"></span><span class="brand-name">PeakMotion Chiropractic</span></div>
  <div class="deco-circle"></div>
  <div class="body">
    <h2>Lorem ipsum</h2>
    <p>Lorem ipsum dolor sit amet, consectetur adipiscing elit. Duis in justo lacus. Morbi vitae urna ante, id mattis ligula. Donec nunc mi, hendrerit sed pulvinar in, tincidunt non nibh. Maecenas volutpat vehicula lacus ac semper.</p>
    <p>Nunc sed purus nunc. Sed feugiat sapien. Integer lobortis convallis urna, vel ultrices sit amet. Nunc justo sem, consectetur pharetra condimentum eu, posuere semper neque. Vivamus congue pretium massa, eu ornare dui vehicula nec.</p>
    <p>Cras viverra nunc a sem fringilla, vitae laoreet tortor ultrices. Etiam hendrerit nunc ut nulla ultrices aliquet. Praesent nec augue quis nibh bibendum mattis. Pellentesque habitant morbi tristique senectus et netus.</p>
    <p>Aliquam erat volutpat. Quisque mollis tortor at velit faucibus, a commodo magna placerat. Donec porta, nisi non tincidunt aliquet, turpis erat imperdiet ipsum, quis aliquam tellus elit eu arcu.</p>
  </div>
</section>

<section class="sheet envelope" aria-label="Envelope">
  <div class="tagline-band"><span class="tagline">Work hard. Play hard. Safe guard</span></div>
  <div class="brand"><span class="brand-dot"></span><span class="brand-name">PeakMotion Chiropractic</span></div>
  <div class="deco-circle"></div>
</section>

<section class="sheet appointment-card" aria-label="Appointment card">
  <div class="brand"><span class="brand-dot"></span><span class="brand-name">PeakMotion Chiropractic</span></div>
  <div class="deco-circle"></div>
  <div class="fields">
    <div class="field">Day:<span></span></div>
    <div class="field">Date:<span></span></div>
    <div class="field">Time:<span></span></div>
  </div>
  <div class="tagline-band"><span class="tagline">Work hard. Play hard. Safe guard</span></div>
</section>

<section class="sheet business-card" aria-label="Business card">
  <div class="tagline-band"><span class="tagline">Work hard. Play hard. Safe guard</span></div>
  <div class="brand"><span class="brand-dot"></span><span class="brand-name">PeakMotion Chiropractic</span></div>
  <div class="deco-circle"></div>
  <div class="person">Colin R Dembry D.C.</div>
  <div class="contact">
    5917 S 420 E Bld. 200 Ste C.<br>
    Hollin Ridge, IN 46273<br>
    (inside Norrin Callow Fitness Center)<br>
    <span class="label">phone</span> (555) 310-4821<br>
    <span class="label">fax</span> (555) 310-4822<br>
    dembrydc@qvmail.example
  </div>
</section>

</body>
</html>
```